Update Pulp Parlor menu board to appear Fresh and modern

I need a menu board design that is not cluttered, easy to read, playful and the style of healthy and fresh for a juice bar. I will be editing the details of the items, so basically the design is all I need. I prefer the files to be in Microsoft Publisher as I am most familiar, but I have illustrator as well, but not as advanced on that. The size should be 36"x36". I will create 3 seperate boards from the one design.

Target Market(s)

health concious people, active lifestyle people

Font styles to use
Serif

Colors

Designer to choose colors to be used in the design.

Requirements
Must have
• Not cluttered
• Modern feel
Nice to have
• i like the style of the
• "cold pressed juice" part of my attached juice bottle label

```html
<!DOCTYPE html>
<html lang="en">
<head>
<meta charset="utf-8">
<title>Pulp Parlor Menu Board</title>
<link rel="stylesheet" href="https://fonts.googleapis.com/css2?family=Alfa+Slab+One&family=Josefin+Sans:wght@300&family=Teko:wght@500;600&family=Open+Sans:wght@700&family=Oswald:wght@500&display=swap">
<style>
  :root{
    --cream:#f1efe7;
    --ink:#2b2b2b;
    --orange:#f06a26;
    --green:#11a24c;
    --magenta:#c3238c;
    --tag:#3f3f3f;
    --tag-text:#ffe800;
    --rule:#555;
  }
  *{margin:0;padding:0;box-sizing:border-box}
  html,body{width:1200px;height:1200px;overflow:hidden;background:var(--cream)}
  .board{position:relative;width:1200px;height:1200px;background:var(--cream);font-family:"Open Sans",sans-serif;color:var(--ink)}
  .header-art{position:absolute;left:0;top:0;width:1200px;height:260px}
  .brand-name{position:absolute;left:0;top:78px;width:1200px;text-align:center;font-family:"Open Sans",sans-serif;font-weight:700;font-size:58px;line-height:64px;color:var(--ink);text-transform:uppercase;letter-spacing:2px}
  .divider{position:absolute;top:231px;width:2px;height:893px;background:var(--rule)}
  .col-head{position:absolute;top:228px}
  .col-head .light{font-family:"Josefin Sans",sans-serif;font-weight:300;font-size:58px;line-height:56px;letter-spacing:3px}
  .col-head .heavy{font-family:"Alfa Slab One",serif;font-size:56px;line-height:60px;letter-spacing:1px}
  .col-head .heavy2{font-family:"Alfa Slab One",serif;font-size:56px;line-height:56px;letter-spacing:1px}
  .cold{color:var(--orange)} .warm{color:var(--green)} .brk{color:var(--magenta)}
  .item{position:absolute;width:330px}
  .item h3{font-family:"Teko",sans-serif;font-weight:600;font-size:31px;line-height:26px;letter-spacing:.5px;text-transform:uppercase;padding-top:4px}
  .item p{font-family:"Open Sans",sans-serif;font-weight:700;font-size:12px;line-height:16.4px;text-transform:uppercase;margin-top:2px;color:var(--ink)}
  .item .note{font-size:8px;line-height:11px;color:var(--orange);text-transform:none;margin-top:0}
  .prices{display:grid;grid-template-columns:repeat(3,50px);column-gap:9px;margin-top:4px}
  .prices.two{grid-template-columns:repeat(2,50px)}
  .tag{background:var(--tag);color:var(--tag-text);font-size:10.5px;line-height:15px;text-align:center;font-weight:700}
  .price{font-family:"Oswald",sans-serif;font-weight:500;font-size:27px;line-height:34px;text-align:center;color:var(--ink);transform:scaleX(.8)}
  .served{position:absolute;left:803px;top:1086px;font-family:"Alfa Slab One",serif;font-size:26px;letter-spacing:2px;color:var(--magenta)}
</style>
</head>
<body>
<div class="board">
  <svg class="header-art" viewBox="0 0 1200 260" role="img" aria-label="Weathered wood planks with sprigs of green leaves">
    <defs>
      <linearGradient id="wood" x1="0" y1="0" x2="1" y2="1">
        <stop offset="0" stop-color="#cdb698"/>
        <stop offset=".5" stop-color="#dcc9ad"/>
        <stop offset="1" stop-color="#bfa684"/>
      </linearGradient>
    </defs>
    <rect width="1200" height="260" fill="url(#wood)"/>
    <path d="M0 248 Q600 40 1200 248 L1200 260 L0 260Z" fill="#7e7468" opacity=".55"/>
    <path d="M0 246 Q600 58 1200 246 L1200 260 L0 260Z" fill="var(--cream)"/>
  </svg>

  <div class="brand-name">Pulp Parlor</div>

  <div class="divider" style="left:97px"></div>
  <div class="divider" style="left:445px"></div>
  <div class="divider" style="left:791px"></div>

  <div class="col-head cold" style="left:110px"><div class="light">COLD</div><div class="heavy">WRAPS</div></div>
  <div class="col-head warm" style="left:457px"><div class="light">WARM</div><div class="heavy">WRAPS</div></div>
  <div class="col-head brk" style="left:803px"><div class="heavy2" style="margin-top:6px">BREAK</div><div class="heavy2">FAST</div></div>

  <div class="item cold" style="left:110px;top:362px">
    <h3>BLT Ranch Wrap</h3>
    <p>Roasted red pepper hummus,<br>Kalamata olives, spring mix,<br>tomato on a wheat tortilla</p>
    <p class="note">Add Chicken to a Sm/Reg 1.50 &nbsp;Lrg 2.50</p>
    <div class="prices"><span class="tag">Small</span><span class="tag">Regular</span><span class="tag">Large</span><span class="price">5</span><span class="price">6.75</span><span class="price">8.75</span></div>
  </div>
  <div class="item cold" style="left:110px;top:531px">
    <h3>Pesto Wrap</h3>
    <p>Grilled chicken breast, spring<br>mix, tomatoes, sun dried<br>tomato pesto</p>
    <div class="prices"><span class="tag">Small</span><span class="tag">Regular</span><span class="tag">Large</span><span class="price">5</span><span class="price">6.50</span><span class="price">8.25</span></div>
  </div>
  <div class="item cold" style="left:110px;top:686px">
    <h3>Chicken Caesar</h3>
    <p>Grilled chicken breast, romaine<br>lettuce, parmesan, caesar<br>dressing</p>
    <div class="prices"><span class="tag">Small</span><span class="tag">Regular</span><span class="tag">Large</span><span class="price">5</span><span class="price">6.50</span><span class="price">8.25</span></div>
  </div>
  <div class="item cold" style="left:110px;top:841px">
    <h3>Buffalo Chicken</h3>
    <p>Lightly breaded buffalo chicken,<br>mixed greens, tomato, ranch</p>
    <div class="prices"><span class="tag">Small</span><span class="tag">Regular</span><span class="tag">Large</span><span class="price">5</span><span class="price">6.50</span><span class="price">8.25</span></div>
  </div>
  <div class="item cold" style="left:110px;top:980px">
    <h3>Greek Wrap</h3>
    <p>Roasted red pepper hummus,<br>Kalamata olives, spring mix,<br>tomato on a wheat tortilla</p>
    <p class="note">Add Chicken to a Small 1.50 or Large 2.50</p>
    <div class="prices two"><span class="tag">Regular</span><span class="tag">Large</span><span class="price">4.75</span><span class="price">7.50</span></div>
  </div>

  <div class="item warm" style="left:457px;top:362px">
    <h3>Cheese Steak Wrap</h3>
    <p>Thinly sliced beef, onions,<br>peppers and cheddar jack cheese</p>
    <div class="prices two"><span class="tag">Regular</span><span class="tag">Large</span><span class="price">7.50</span><span class="price">15</span></div>
  </div>
  <div class="item warm" style="left:457px;top:501px">
    <h3>BBQ Chicken Wrap</h3>
    <p>Chicken breast, bacon, onion<br>strings, BBQ sauce and cheddar<br>jack cheese</p>
    <div class="prices two"><span class="tag">Regular</span><span class="tag">Large</span><span class="price">8</span><span class="price">15.50</span></div>
  </div>
  <div class="item warm" style="left:457px;top:656px">
    <h3>Philly Chicken Wrap</h3>
    <p>Chicken breast, onions, peppers<br>and cheddar jack cheese</p>
    <div class="prices two"><span class="tag">Regular</span><span class="tag">Large</span><span class="price">6.75</span><span class="price">12.50</span></div>
  </div>
  <div class="item warm" style="left:457px;top:795px">
    <h3>Venetian Chicken Wrap</h3>
    <p>Grilled chicken breast, roasted<br>red peppers, tomato, cheddar<br>jack cheese and sun dried<br>tomato pesto</p>
    <div class="prices two"><span class="tag">Regular</span><span class="tag">Large</span><span class="price">6.75</span><span class="price">12.50</span></div>
  </div>
  <div class="item warm" style="left:457px;top:967px">
    <h3>Chicken &amp; Broccoli</h3>
    <p>Grilled chicken breast, steamed<br>broccoli and cheddar jack<br>cheese</p>
    <div class="prices two"><span class="tag">Regular</span><span class="tag">Large</span><span class="price">6.75</span><span class="price">12.50</span></div>
  </div>

  <div class="item brk" style="left:803px;top:362px">
    <h3>Bacon Burrito</h3>
    <p>Bacon, scrambled eggs,<br>potato, cheese with green chili</p>
    <div class="prices two"><span class="tag">Regular</span><span class="tag">Large</span><span class="price">5.50</span><span class="price">10</span></div>
  </div>
  <div class="item brk" style="left:803px;top:501px">
    <h3>Sausage Burrito</h3>
    <p>Sausage, scrambled eggs,<br>potato, cheese, green chili</p>
    <div class="prices two"><span class="tag">Regular</span><span class="tag">Large</span><span class="price">5.50</span><span class="price">10</span></div>
  </div>
  <div class="item brk" style="left:803px;top:640px">
    <h3>Meat &amp; Potatoes Burrito</h3>
    <p>Philly beef, scrambled eggs,<br>potato, cheese, green chili</p>
    <div class="prices two"><span class="tag">Regular</span><span class="tag">Large</span><span class="price">7.50</span><span class="price">15</span></div>
  </div>
  <div class="item brk" style="left:803px;top:779px">
    <h3>Bean Breakfast Burrito</h3>
    <p>Scrambled eggs, refried beans,<br>green chili, potato, cheese</p>
    <div class="prices two"><span class="tag">Regular</span><span class="tag">Large</span><span class="price">5.50</span><span class="price">10</span></div>
  </div>
  <div class="item brk" style="left:803px;top:918px">
    <h3>Veggie Omelet Burrito</h3>
    <p>Scrambled eggs, spinach, roasted<br>red peppers, tomato, cheese,<br>green chili on a wheat tortilla</p>
    <div class="prices two"><span class="tag">Regular</span><span class="tag">Large</span><span class="price">5.50</span><span class="price">10</span></div>
  </div>

  <div class="served">SERVED ALL DAY</div>
</div>
</body>
</html>
```